VELT needs a simple, contemporary and easy to use 'designer' website (fully working/coded)

VELT is a progressive market research consultancy based in Sydney, Australia. We are a new company and require a contemporary/modern and bold, uncomplicated/simple, clean/uncluttered site, which uses friendly and easy to read fonts. The brand is approachable. The colour palate should be simple and contemporary. Colours used in our logo are:#FFCC00 and #404041 so any others should complement these.

The following website gives a really good idea of how simple the site should be: www.brightmarrow.com.au and I am looking to create something similar to this style of site (but not necessarily copied).

The website should convey ‘different types of customer’. VELT helps different companies ‘connect’ with their particular shoppers or end users of their product. This could be a mum doing the washing, a dad cleaning the car, children eating ice cream, old people reading the newspaper, someone trying on glasses, someone buying petfood etc. Alternatively it could simply just be pictures of different people…different ages, different nationalities, different employment types etc, but they should give a positive impression (ie people smiling/laughing) and also GREAT quality photos.

Content will also be attached but please note this is just a draft reference and will be sent to a copywriter for improvement. The telephone number is yet to be confirmed but will be given at the end of the contest.

The navigation may borrow strongly from www.brightmarrow.com.au. It may have the following navigation panel:

ABOUT US

WHAT WE DO

> NPD

> PRODUCT TESTING

> SHOPPER

> SEGMENTATION

> ONLINE COMMUNITIES

> CUSTOMER EXPERIENCE

> VISUALISATION

> TAILOR MADE

CONTACT US

The home page may be WHAT WE DO and each picture represents one of the 8 sections (such as NPD) etc.

One of my main objectives is also to get people to sign up to my quarterly newsletter, so would like to make this very visible, and make it easy for them to connect via workmesh.

I will also want to add a blog page in September (so needs to be hidden now but switched on in Sept). This blog will contain articles from the newsletters and workmesh updates. I may also want to add a simple 90-180 second video at the bottom of each of the 8 sections (to be added over the next 12 months but i would like to ensure it is possible to do this at a later stage).

The logo has recently been designed and i have attcahed different colour versions as i may be swayed depending on hoe they look in te website. I tend to prefer yellow on white, or white on yellow but other optins are included if you think they work better with your design.

Target Market(s)

Professionals in large blue chip companies..such as pino fizz, varona, tamborix etc. Marketing Managers/Directors, PR and advertising agencies etc.

Industry/Entity Type

Progressive

Requirements
Must have
• High quality positive photos. Be very easy to navigate...should scream simple!

```html
<!DOCTYPE html>
<html lang="en">
<head>
<meta charset="utf-8">
<title>VELT – New Product Development</title>
<link href="https://fonts.googleapis.com/css2?family=Open+Sans:wght@400;600;700&display=swap" rel="stylesheet">
<style>
:root{
  --bg:#111112;
  --panel:#1b1b1c;
  --bar:#262627;
  --yellow:#ffcc00;
  --charcoal:#404041;
  --text:#e6e6e6;
  --muted:#9a9a9a;
  --rule:#3a3a3b;
}
*{box-sizing:border-box;margin:0;padding:0}
html,body{width:829px;height:1200px;overflow:hidden;background:var(--bg);font-family:'Open Sans',Arial,sans-serif;color:var(--text)}
.page{position:relative;width:829px;height:1200px}
.topbar{position:absolute;left:0;top:0;width:829px;height:46px;background:var(--bar);display:flex;align-items:center;padding-left:20px}
.nav a{color:var(--muted);font-size:12px;text-decoration:none;margin-right:26px}
.nav a.active{color:var(--yellow)}
.brand{position:absolute;right:24px;top:10px;color:var(--yellow);font-weight:700;font-size:22px;line-height:26px}
.sidebar{position:absolute;left:20px;top:90px;width:150px}
.sidebar h1{color:var(--yellow);font-size:21px;font-weight:700;line-height:1.2}
.share{display:flex;align-items:center;gap:6px;margin-top:12px;font-size:11px;color:var(--muted)}
.share i{width:10px;height:10px;border-radius:50%;background:var(--muted);display:block}
.pager{position:absolute;right:20px;top:88px;display:flex;gap:4px}
.pager span{width:20px;height:20px;background:var(--charcoal);display:flex;align-items:center;justify-content:center}
.content{position:absolute;left:193px;top:98px;width:484px;font-size:10.5px;line-height:1.55;text-align:center;color:var(--text)}
.intro{padding-bottom:14px;border-bottom:1px solid var(--rule);margin-bottom:22px}
.content h2{color:var(--yellow);font-size:12px;font-weight:700;margin:16px 0 6px}
.content p+p{margin-top:10px}
.cols{display:flex;gap:30px;margin-top:8px}
.cols div{flex:1}
.gallery{position:absolute;left:0;top:685px;width:829px;height:420px;display:grid;grid-template-columns:repeat(4,1fr);grid-template-rows:1fr 1fr;gap:3px}
.photo{display:block}
.footer{position:absolute;left:0;top:1105px;width:829px;height:95px;background:var(--panel);display:flex;align-items:center;justify-content:space-between;padding:0 20px}
.footer small{font-size:9px;color:var(--muted)}
.footer .social{width:18px;height:18px;border-radius:50%;background:var(--charcoal)}
</style>
</head>
<body>
<div class="page">
  <header class="topbar">
    <nav class="nav"><a class="active" href="#">What We Do</a><a href="#">About Us</a><a href="#">Contact Us</a></nav>
    <div class="brand">VELT</div>
  </header>

  <aside class="sidebar">
    <h1>New Product Development</h1>
    <div class="share"><i></i>Share</div>
  </aside>

  <div class="pager">
    <span><svg width="8" height="10" viewBox="0 0 8 10"><path d="M6 1L2 5l4 4" stroke="#ccc" stroke-width="1.5" fill="none"/></svg></span>
    <span><svg width="8" height="10" viewBox="0 0 8 10"><path d="M2 1l4 4-4 4" stroke="#ccc" stroke-width="1.5" fill="none"/></svg></span>
  </div>

  <main class="content">
    <p class="intro">From idea screening to the final product – we've got it covered! We provide commercial recommendations to help clients generate more successful product launches whether it's concept, product, packaging, claims, price evaluation or full mix optimisation.</p>

    <h2>Concept:</h2>
    <p>We can evaluate a mass of early stage ideas and identify the strongest ideas for further consideration, as well as optimise more developed concepts. All ideas can be tested quickly and cost-efficiently online, either at general population level or among a more focused target group. We use trusted and tested key measures and often employ more interactive techniques to obtain detailed diagnostic information to help understand your ideas to ensure they have the greatest possible appeal. We can provide clarity on whether a concept has the potential to succeed in market, who the target audience should be, where sources of volume will come from, and understand what variants would optimise the range.</p>

    <h2>Packaging:</h2>
    <p>We adopt sophisticated on-line research techniques to effectively measure the impact of packaging, including interactive shelf environments. Where touch and feel is considered important, we conduct central location tests.</p>
    <p>We can understand whether new packaging will perform more sales than the current design, measure whether the new pack will create better standout in a competitive fixture, and understand whether the packaging will bring in new consumers (and whether there is a threat of alienating current consumers).</p>

    <div class="cols">
      <div>
        <h2>Pricing:</h2>
        <p>We use a range of approaches to understand pricing depending on the stage of testing. These range from the more pragmatic technique such as PSM (Van Westendorp) or monadic controlled (group) testing, through to more sophisticated choice modelling.</p>
      </div>
      <div>
        <h2>Product:</h2>
        <p>Products can be tested in home or at a central location, either in a monadic (each person only tests one product) or in a sequential monadic (several products tested) order. Product testing can range from simple pragmatic benchmarking, through to detailed sensory analysis.</p>
      </div>
    </div>
  </main>

  <section class="gallery">
    <span class="photo" role="img" aria-label="Smiling man in a blue shirt" style="background:linear-gradient(135deg,#6d7f96,#c9b8a2)"></span>
    <span class="photo" role="img" aria-label="Woman shopping with colourful bags" style="background:linear-gradient(135deg,#b0416a,#e6b64a)"></span>
    <span class="photo" role="img" aria-label="Woman browsing a supermarket aisle" style="background:linear-gradient(135deg,#8a9a6b,#d8cdb4)"></span>
    <span class="photo" role="img" aria-label="Woman holding a glass of wine" style="background:linear-gradient(135deg,#5d3a2c,#caa07a)"></span>
    <span class="photo" role="img" aria-label="Laughing woman talking on the phone" style="background:linear-gradient(135deg,#cfc4b6,#8e7a66)"></span>
    <span class="photo" role="img" aria-label="Family relaxing on a sofa at home" style="background:linear-gradient(135deg,#e5ddd0,#9f8c76)"></span>
    <span class="photo" role="img" aria-label="Friends smiling together outdoors" style="background:linear-gradient(135deg,#b48a68,#e3d6c0)"></span>
    <span class="photo" role="img" aria-label="Older couple smiling together" style="background:linear-gradient(135deg,#6a7e8c,#d6cfc4)"></span>
  </section>

  <footer class="footer">
    <small>© 2013 VELT Market Research</small>
    <span class="social" aria-label="workmesh"></span>
  </footer>
</div>
</body>
</html>
```